Business Card Design for company

We want new business cards. We'd like something different-- yet still highly professional. Our tagline is Providing leadership, delivering success. Stock photos are ok, as long as they are relevant and look upscale.

Target Market(s)

Architecture/Business Management Consulting/Engineering Consulting

Contact Information for Business Card

dark gray background with pops of blue might be good, but you tell me. You're the designers. Rounded corners might be nice, but again, you tell me.

Font styles to use
Serif
Sans Serif

Colors
3276b5
5c5c5c
9d9d9d
fbfbfb

Requirements
Nice to have
• Something different, but still very professional.

```html
<!DOCTYPE html>
<html lang="en">
<head>
<meta charset="utf-8">
<title>Norvale Group – Business Card</title>
<link href="https://fonts.googleapis.com/css2?family=Open+Sans:wght@400;600&display=swap" rel="stylesheet">
<style>
  :root {
    --blue: #2f6fa8;
    --blue-deep: #245c90;
    --blue-light: #3276b5;
    --grey-dark: #5c5c5c;
    --grey-mid: #9d9d9d;
    --paper: #fbfbfb;
    --backdrop: #e9e7e3;
    --ink: #1d1d1d;
  }
  html, body {
    margin: 0;
    padding: 0;
    width: 1200px;
    height: 1023px;
    overflow: hidden;
    background: var(--backdrop);
    font-family: "Open Sans", Arial, sans-serif;
  }
  .canvas {
    position: relative;
    width: 1200px;
    height: 1023px;
  }
  .card {
    position: absolute;
    left: 240px;
    width: 720px;
    height: 411px;
    border-radius: 6px;
    overflow: hidden;
    background: var(--paper);
    box-shadow: 0 6px 18px rgba(0,0,0,0.18);
  }
  .card--front { top: 67px; }
  .card--back  { top: 545px; }
  .card svg { position: absolute; inset: 0; }

  .brand {
    position: absolute;
    display: flex;
    align-items: center;
    gap: 12px;
    white-space: nowrap;
  }
  .brand__mark {
    flex: none;
    width: 24px;
    height: 24px;
    background: var(--blue-light);
  }
  .brand__name {
    font-weight: 600;
    font-size: 34px;
    letter-spacing: 2px;
    color: var(--grey-dark);
    line-height: 1;
  }
  .card--front .brand { left: 190px; top: 96px; }
  .card--back .brand { left: 110px; top: 187px; }

  .holder {
    position: absolute;
    left: 40px;
    top: 196px;
  }
  .holder__name {
    margin: 0;
    font-weight: 600;
    font-size: 24px;
    color: var(--ink);
  }
  .holder__role {
    margin: 2px 0 0;
    font-size: 17px;
    color: var(--grey-dark);
  }

  .contact {
    position: absolute;
    left: 240px;
    top: 286px;
    margin: 0;
    padding: 0;
    list-style: none;
    color: #fff;
    font-size: 15.5px;
    line-height: 22px;
  }
  .contact__item {
    display: flex;
    align-items: flex-start;
    gap: 10px;
  }
  .contact__icon {
    flex: none;
    width: 14px;
    height: 14px;
    margin-top: 4px;
    background: #fff;
    border-radius: 2px;
  }
  .contact__icon svg { position: static; display: block; }
</style>
</head>
<body>
<main class="canvas">

  <section class="card card--front" aria-label="Business card front">
    <svg width="720" height="411" viewBox="0 0 720 411">
      <path class="wave-grey" fill="var(--grey-dark)"
        d="M170 411 C140 320 205 238 320 232 C470 224 560 210 610 130 C640 80 655 35 668 0 L720 0 L720 411 Z"/>
      <path class="wave-blue" fill="var(--blue)" stroke="var(--paper)" stroke-width="6"
        d="M205 414 C180 330 235 270 335 264 C480 256 580 240 635 150 C665 100 685 45 698 -4 L724 -4 L724 414 Z"/>
    </svg>

    <div class="brand">
      <span class="brand__mark"></span>
      <span class="brand__name">NORVALE GROUP</span>
    </div>

    <div class="holder">
      <p class="holder__name">Daniel Reyes</p>
      <p class="holder__role">Owner</p>
    </div>

    <ul class="contact">
      <li class="contact__item">
        <span class="contact__icon"><svg width="14" height="14" viewBox="0 0 14 14"><path d="M4 3 L6 5 L5 6.5 Q6.5 8.5 7.5 9 L9 8 L11 10 L9.5 11.5 Q5 10.5 2.5 4.5 Z" fill="var(--blue)"/></svg></span>
        <span>+0000-0000-0000</span>
      </li>
      <li class="contact__item">
        <span class="contact__icon"><svg width="14" height="14" viewBox="0 0 14 14"><rect x="2.5" y="4" width="9" height="6" fill="none" stroke="var(--blue)" stroke-width="1.2"/><path d="M2.5 4 L7 7.5 L11.5 4" fill="none" stroke="var(--blue)" stroke-width="1.2"/></svg></span>
        <span>info@yourdomain.com</span>
      </li>
      <li class="contact__item">
        <span class="contact__icon"><svg width="14" height="14" viewBox="0 0 14 14"><circle cx="7" cy="7" r="4.2" fill="none" stroke="var(--blue)" stroke-width="1.2"/><path d="M2.8 7 H11.2 M7 2.8 V11.2" stroke="var(--blue)" stroke-width="1"/></svg></span>
        <span>www.yourdomain.com</span>
      </li>
      <li class="contact__item">
        <span class="contact__icon"><svg width="14" height="14" viewBox="0 0 14 14"><path d="M7 12 Q3.5 7.5 3.5 5.5 A3.5 3.5 0 0 1 10.5 5.5 Q10.5 7.5 7 12 Z" fill="var(--blue)"/><circle cx="7" cy="5.5" r="1.3" fill="#fff"/></svg></span>
        <span>Suite 210, 48 Harbour Lane,<br>Bristol</span>
      </li>
    </ul>
  </section>

  <section class="card card--back" aria-label="Business card back">
    <svg width="720" height="411" viewBox="0 0 720 411">
      <rect width="720" height="411" fill="var(--blue)"/>
      <path fill="var(--grey-dark)" d="M0 0 H520 C600 90 610 320 540 411 H0 Z"/>
      <path fill="var(--paper)" d="M0 0 H490 C565 90 575 320 510 411 H0 Z"/>
    </svg>
    <div class="brand">
      <span class="brand__mark"></span>
      <span class="brand__name">NORVALE GROUP</span>
    </div>
  </section>

</main>
</body>
</html>
```